New Zealand Marlborough Sauvignon Blanc wine packaging design

We need packaging design for our new wine brand, Dunmore Hale. The wine is a New Zealand Marlborough Sauvignon Blanc. We would like the packaging will portray elegance and style with an understated label. We are looking for a label that portrays the elegance of the French Riviera. The label should be round or pill shaped.
Updates

Industry/Entity Type

Wine

Font styles to use
Serif
Sans Serif

Requirements
Must have
• The words in order of importance: Dunmore Hale, Sauvignon Blanc, Marlborough, New Zealand. It should be fit to the bottle posted in the links
Nice to have
• a pill shape or circular shape
Should not have
• Illustrations of wine bottles, wine glasses, or grapes

```html
<!DOCTYPE html>
<html lang="en">
<head>
<meta charset="utf-8">
<title>Dunmore Hale – Sauvignon Blanc Labels</title>
<link href="https://fonts.googleapis.com/css2?family=Cinzel+Decorative:wght@400;700&family=Montserrat:wght@400;600;700;800&display=swap" rel="stylesheet">
<style>
  :root{
    --gold:#c9992f;
    --ink:#000000;
    --wine:#9b0a0a;
    --paper:#fcf7f5;
    --white:#ffffff;
    --line-grey:#cfcfcf;
    --sketch-light:#f2f2f2;
    --sketch-dark:#9a9a9a;
  }
  *{box-sizing:border-box;margin:0;padding:0}
  html,body{width:1199px;height:1200px;overflow:hidden;background:var(--paper)}
  .canvas{position:relative;width:1199px;height:1200px;overflow:hidden;background:var(--paper);font-family:"Montserrat",sans-serif}

  /* header */
  .masthead{position:absolute;left:0;top:0;width:1199px;height:127px;background:var(--ink)}
  .masthead__dot{position:absolute;top:24px;width:72px;height:72px;border-radius:50%;background:var(--gold)}
  .masthead__dot--left{left:102px}
  .masthead__dot--right{left:1020px}
  .masthead__title{position:absolute;left:0;right:0;top:14px;text-align:center;font-family:"Cinzel Decorative",serif;font-weight:400;font-size:74px;line-height:100px;color:var(--gold);letter-spacing:1px}

  .tagline{position:absolute;left:0;right:0;top:163px;text-align:center;font-weight:700;font-size:21px;letter-spacing:17px;color:var(--gold);padding-left:17px}

  /* round labels */
  .seal{position:absolute;top:316px;width:168px;height:168px;border-radius:50%;border:5px solid var(--ring);background:var(--fill);overflow:hidden}
  .seal__mark{position:absolute;left:50%;top:26px;width:28px;height:28px;margin-left:-14px;border-radius:50%;background:var(--mark)}
  .seal__band{position:absolute;left:0;right:0;top:68px;height:30px;background:var(--ink);border-top:3px solid var(--ring);border-bottom:3px solid var(--ring);font-family:"Cinzel Decorative",serif;font-size:15px;line-height:24px;text-align:center;color:var(--white);white-space:nowrap}
  .seal__variety{position:absolute;left:0;right:0;top:107px;text-align:center;font-size:6.5px;font-weight:700;letter-spacing:3.4px;color:var(--text);padding-left:3px}
  .seal__rule{position:absolute;left:50%;top:119px;width:76px;margin-left:-38px;height:1px;background:var(--text)}
  .seal__rule::after{content:"";position:absolute;left:50%;top:-2px;width:4px;height:4px;margin-left:-2px;background:var(--text);transform:rotate(45deg)}
  .seal__origin{position:absolute;left:0;right:0;top:125px;text-align:center;font-size:6.4px;color:var(--text)}

  .theme-noir{--ring:var(--gold);--fill:var(--ink);--mark:var(--white);--text:var(--gold)}
  .theme-claret{--ring:var(--wine);--fill:var(--white);--mark:var(--wine);--text:var(--ink)}
  .theme-ivory{--ring:var(--gold);--fill:var(--white);--mark:var(--ink);--text:var(--gold)}

  /* pill labels */
  .pill{position:absolute;top:526px;width:245px;height:416px;border-radius:122px;background:var(--white);border:1px solid var(--line-grey)}
  .pill__frame{position:absolute;left:10px;top:10px;width:223px;height:394px;border-radius:112px;border:5px solid var(--frame);box-shadow:inset 0 0 0 2px var(--white),inset 0 0 0 4px var(--gold);overflow:hidden;background:var(--white)}
  .pill__mark{position:absolute;z-index:2;left:50%;top:40px;width:28px;height:28px;margin-left:-14px;border-radius:50%;background:var(--markc)}
  .pill__scene{position:absolute;left:12px;right:12px;top:90px;height:108px;background:linear-gradient(180deg,var(--white) 0%,var(--sketch-light) 40%,var(--sketch-dark) 100%)}
  .pill__scene--tall{top:76px;height:122px}
  .pill__band{position:absolute;left:0;right:0;top:200px;height:42px;background:var(--bandc);border-top:2px solid var(--gold);border-bottom:2px solid var(--gold);font-family:"Cinzel Decorative",serif;font-size:19.5px;line-height:38px;text-align:center;color:var(--namec);white-space:nowrap}
  .pill__ornament{position:absolute;left:0;right:0;top:264px;height:20px;background:var(--ornc);opacity:.85}
  .pill__variety{position:absolute;left:0;right:0;top:296px;text-align:center;font-size:9px;font-weight:700;letter-spacing:5.6px;color:var(--textc);padding-left:5px}
  .pill__rule{position:absolute;left:50%;top:312px;width:120px;margin-left:-60px;height:1px;background:var(--textc)}
  .pill__rule::after{content:"";position:absolute;left:50%;top:-2px;width:5px;height:5px;margin-left:-2.5px;background:var(--textc);transform:rotate(45deg)}
  .pill__origin{position:absolute;left:0;right:0;top:322px;text-align:center;font-size:9.6px;color:var(--textc)}
  .pill__fan{position:absolute;left:50%;top:348px;width:52px;height:26px;margin-left:-26px;border-radius:0 0 26px 26px;background:var(--ink)}

  .pill--noir{--frame:var(--ink);--markc:var(--gold);--bandc:var(--ink);--namec:var(--white);--ornc:var(--gold);--textc:var(--gold)}
  .pill--claret{--frame:var(--wine);--markc:var(--wine);--bandc:var(--wine);--namec:var(--white);--ornc:var(--ink);--textc:var(--ink)}
  .pill--ivory{--frame:var(--ink);--markc:var(--gold);--bandc:var(--white);--namec:var(--ink);--ornc:var(--gold);--textc:var(--gold)}
  .pill--ivory .pill__band{border-color:var(--white)}

  /* footer */
  .footer-banner{position:absolute;left:90px;top:1137px;width:1019px;height:63px;background:var(--gold);clip-path:polygon(2.5% 0,97.5% 0,100% 100%,0 100%)}
  .footer-banner__text{position:absolute;left:0;right:0;top:1147px;text-align:center;font-weight:800;font-size:32px;letter-spacing:24px;padding-left:24px;color:var(--ink);line-height:44px}
</style>
</head>
<body>
<div class="canvas">

  <header class="masthead">
    <span class="masthead__dot masthead__dot--left"></span>
    <h1 class="masthead__title">DUNMORE HALE</h1>
    <span class="masthead__dot masthead__dot--right"></span>
  </header>

  <p class="tagline">QUALITY PREMIUM</p>

  <div class="seal theme-noir" style="left:72px">
    <span class="seal__mark"></span>
    <div class="seal__band">DUNMORE HALE</div>
    <p class="seal__variety">SAUVIGNON BLANC</p>
    <span class="seal__rule"></span>
    <p class="seal__origin">Marlborough, Nueva Zelanda</p>
  </div>
  <div class="seal theme-claret" style="left:365px">
    <span class="seal__mark"></span>
    <div class="seal__band">DUNMORE HALE</div>
    <p class="seal__variety">SAUVIGNON BLANC</p>
    <span class="seal__rule"></span>
    <p class="seal__origin">Marlborough, Nueva Zelanda</p>
  </div>
  <div class="seal theme-ivory" style="left:666px">
    <span class="seal__mark"></span>
    <div class="seal__band">DUNMORE HALE</div>
    <p class="seal__variety">SAUVIGNON BLANC</p>
    <span class="seal__rule"></span>
    <p class="seal__origin">Marlborough, Nueva Zelanda</p>
  </div>
  <div class="seal theme-noir" style="left:963px">
    <span class="seal__mark"></span>
    <div class="seal__band">DUNMORE HALE</div>
    <p class="seal__variety">SAUVIGNON BLANC</p>
    <span class="seal__rule"></span>
    <p class="seal__origin">Marlborough, Nueva Zelanda</p>
  </div>

  <div class="pill pill--noir" style="left:29px">
    <div class="pill__frame">
      <span class="pill__mark"></span>
      <div class="pill__scene" role="img" aria-label="Pen sketch of a Riviera village with a clock tower"></div>
      <div class="pill__band">DUNMORE HALE</div>
      <div class="pill__ornament" role="img" aria-label="Gold Art Deco diamond border"></div>
      <p class="pill__variety">SAUVIGNON BLANC</p>
      <span class="pill__rule"></span>
      <p class="pill__origin">Marlborough, Nueva Zelanda</p>
    </div>
  </div>

  <div class="pill pill--claret" style="left:327px;top:532px">
    <div class="pill__frame">
      <span class="pill__mark"></span>
      <div class="pill__scene pill__scene--tall" role="img" aria-label="Pen sketch of a seaside promenade with palm trees"></div>
      <div class="pill__band">DUNMORE HALE</div>
      <div class="pill__ornament" role="img" aria-label="Black Art Deco diamond border"></div>
      <p class="pill__variety">SAUVIGNON BLANC</p>
      <span class="pill__rule"></span>
      <p class="pill__origin">Marlborough, Nueva Zelanda</p>
      <div class="pill__fan" role="img" aria-label="Black Art Deco fan ornament"></div>
    </div>
  </div>

  <div class="pill pill--ivory" style="left:625px;top:534px">
    <div class="pill__frame">
      <span class="pill__mark"></span>
      <div class="pill__scene" role="img" aria-label="Pen sketch of a Riviera village with a clock tower"></div>
      <div class="pill__band">DUNMORE HALE</div>
      <div class="pill__ornament" role="img" aria-label="Gold Art Deco diamond border"></div>
      <p class="pill__variety">SAUVIGNON BLANC</p>
      <span class="pill__rule"></span>
      <p class="pill__origin">Marlborough, Nueva Zelanda</p>
    </div>
  </div>

  <div class="pill pill--noir" style="left:925px;top:535px">
    <div class="pill__frame">
      <span class="pill__mark"></span>
      <div class="pill__scene pill__scene--tall" role="img" aria-label="Pen sketch of a coastal town overlooking a bay"></div>
      <div class="pill__band">DUNMORE HALE</div>
      <div class="pill__ornament" style="top:274px" role="img" aria-label="Gold Art Deco diamond border"></div>
      <p class="pill__variety" style="top:306px">SAUVIGNON BLANC</p>
      <span class="pill__rule" style="top:322px"></span>
      <p class="pill__origin" style="top:332px">Marlborough, Nueva Zelanda</p>
    </div>
  </div>

  <div class="footer-banner"></div>
  <p class="footer-banner__text">PROFESSIONAL DESIGN</p>

</div>
</body>
</html>
```